LET ME HANDLE YOUR AUCTION NEEDS!

I am here to handle all your auction needs, I have over 20 years of auction experience buying and selling for dealerships in North Carolina and Tennessee. Send me to the sale to either rep your vehicles or let me know what you need and I can be
another set of eyes to help you buy what is hot and bad credit cars are my specialty. You know a car always sells better with a familiar face rather than auction personnel and with my great reputation I will be able to help find the buyers for your aged inventory.
Call me today and let's get started.
Rob Kellner 555-287-6390
(please have pictures of vehicles or an auto auction in the design)

```html
<!DOCTYPE html>
<html lang="en">
<head>
<meta charset="utf-8">
<title>Rob Kellner – Auction Services Print Set</title>
<link href="https://fonts.googleapis.com/css2?family=Oswald:wght@400;600;700&family=Roboto+Condensed:wght@400;700&family=Kaushan+Script&display=swap" rel="stylesheet">
<style>
  :root {
    --bg: #e9e4e2;
    --peach-light: #fbeee6;
    --peach: #eccdbb;
    --rose: #d9a79c;
    --burgundy: #8c1414;
    --dark: #1d0d09;
    --brown: #5a2410;
    --glow: #b5501c;
    --white: #ffffff;
    --script-red: #c0201b;
  }
  * { box-sizing: border-box; margin: 0; padding: 0; }
  html, body { width: 1200px; height: 800px; overflow: hidden; }
  body {
    background: var(--bg);
    position: relative;
    font-family: "Roboto Condensed", "Arial Narrow", sans-serif;
  }

  /* ---------- shared ---------- */
  .piece {
    position: absolute;
    overflow: hidden;
    box-shadow: 0 6px 18px rgba(0,0,0,.25);
  }
  .piece-bg { position: absolute; inset: 0; width: 100%; height: 100%; }
  .photo-slot { position: absolute; border-radius: 6px; }

  /* ---------- business card ---------- */
  .business-card { left: 70px; top: 130px; width: 320px; height: 540px; }
  .business-card .gavel-photo {
    left: 95px; top: 28px; width: 130px; height: 95px;
    background: radial-gradient(ellipse at 50% 60%, #9a5a35, #6b3a22 60%, #e5c2ad 100%);
  }
  .business-card .card-name {
    position: absolute; left: 0; right: 0; top: 135px;
    text-align: center;
    font-family: "Oswald", sans-serif; font-weight: 700;
    font-size: 46px; color: var(--burgundy); letter-spacing: .5px;
  }
  .business-card .card-phone {
    position: absolute; left: 0; right: 0; top: 300px;
    text-align: center;
    font-family: "Oswald", sans-serif; font-weight: 600;
    font-size: 28px; color: var(--white); letter-spacing: 1px;
  }
  .business-card .card-points {
    position: absolute; left: 42px; top: 352px;
    list-style: none; color: #f3e3da; font-size: 15px; line-height: 1.45;
  }
  .card-points li { display: flex; align-items: center; gap: 8px; }
  .card-points svg { width: 12px; height: 12px; flex: none; }
  .business-card .card-call {
    position: absolute; left: 42px; top: 468px;
    font-family: "Kaushan Script", cursive; font-size: 30px; color: var(--script-red);
  }

  /* ---------- postcard ---------- */
  .postcard { left: 440px; top: 140px; width: 700px; height: 500px; }
  .postcard .headline-lead {
    position: absolute; left: 250px; top: 22px;
    font-family: "Roboto Condensed", sans-serif; font-size: 20px;
    color: var(--dark); letter-spacing: .5px;
  }
  .postcard .headline {
    position: absolute; left: 240px; top: 44px;
    font-family: "Oswald", sans-serif; font-weight: 700;
    font-size: 60px; line-height: 1; color: var(--burgundy);
  }
  .postcard .cars-photo {
    left: 250px; top: 120px; width: 420px; height: 160px;
    background: linear-gradient(100deg, #3a4f9e 0%, #5f77c9 28%, #cfd5dc 45%, #4d6fd6 60%, #e0c233 75%, #c92020 92%, #6b2418 100%);
    border-radius: 40px 20px 20px 40px;
  }
  .postcard .gavel-photo {
    left: 50px; top: 200px; width: 140px; height: 100px;
    background: radial-gradient(ellipse at 50% 60%, #a3613a, #5e3018 60%, #2a130b 100%);
  }
  .postcard .call-script {
    position: absolute; left: 240px; top: 286px;
    font-family: "Kaushan Script", cursive; font-size: 24px; line-height: 36px;
    color: var(--white); white-space: nowrap;
  }
  .postcard .experience {
    position: absolute; right: 26px; top: 338px; text-align: right;
    font-family: "Roboto Condensed", sans-serif; color: var(--white);
    font-size: 17px; line-height: 1.1;
  }
  .experience strong { display: block; font-size: 22px; font-weight: 700; }
  .postcard .body-copy {
    position: absolute; left: 240px; top: 330px; width: 290px;
    font-size: 11px; line-height: 1.35; color: #f1e2d8;
  }
  .postcard .contact-strip {
    position: absolute; left: 0; right: 0; bottom: 0; height: 50px;
    display: flex; align-items: center; justify-content: center;
    font-family: "Oswald", sans-serif; font-weight: 700;
    font-size: 24px; color: var(--burgundy); letter-spacing: .5px;
  }
</style>
</head>
<body>

  <!-- Business card -->
  <section class="piece business-card">
    <svg class="piece-bg" viewBox="0 0 320 540" preserveAspectRatio="none" aria-hidden="true">
      <defs>
        <radialGradient id="cardGlow" cx="85%" cy="70%" r="75%">
          <stop offset="0" stop-color="#b5501c"/>
          <stop offset=".45" stop-color="#5a2410"/>
          <stop offset="1" stop-color="#1d0d09"/>
        </radialGradient>
        <linearGradient id="cardTop" x1="0" y1="0" x2="0" y2="1">
          <stop offset="0" stop-color="#eccdbb"/>
          <stop offset="1" stop-color="#fbeee6"/>
        </linearGradient>
      </defs>
      <rect width="320" height="540" fill="url(#cardGlow)"/>
      <path d="M0 0H320V300C220 250 110 225 0 225Z" fill="url(#cardTop)"/>
      <path d="M0 225C110 225 220 250 320 300V312C220 262 110 238 0 238Z" fill="#d9a79c"/>
      <path d="M0 238C110 238 220 262 320 312V318C220 268 110 245 0 245Z" fill="#ffffff" opacity=".7"/>
      <line x1="200" y1="210" x2="310" y2="240" stroke="#8a6a60" stroke-width="2" stroke-dasharray="2 4"/>
    </svg>
    <div class="photo-slot gavel-photo" role="img" aria-label="Photo of an auction gavel resting on its block beside a small red car"></div>
    <h1 class="card-name">ROB KELLNER</h1>
    <p class="card-phone">555.287.6390</p>
    <ul class="card-points">
      <li><svg viewBox="0 0 12 12"><path d="M1 6l3 3 7-7" fill="none" stroke="#fff" stroke-width="2"/></svg>Over 20 years of auction experience</li>
      <li><svg viewBox="0 0 12 12"><path d="M1 6l3 3 7-7" fill="none" stroke="#fff" stroke-width="2"/></svg>Buying and selling for dealerships</li>
      <li><svg viewBox="0 0 12 12"><path d="M1 6l3 3 7-7" fill="none" stroke="#fff" stroke-width="2"/></svg>Bad credit - No Problem</li>
      <li><svg viewBox="0 0 12 12"><path d="M1 6l3 3 7-7" fill="none" stroke="#fff" stroke-width="2"/></svg>Known reputation</li>
      <li><svg viewBox="0 0 12 12"><path d="M1 6l3 3 7-7" fill="none" stroke="#fff" stroke-width="2"/></svg>I can find your buyers!</li>
    </ul>
    <p class="card-call">Call me today!</p>
  </section>

  <!-- Postcard -->
  <section class="piece postcard">
    <svg class="piece-bg" viewBox="0 0 700 500" preserveAspectRatio="none" aria-hidden="true">
      <defs>
        <radialGradient id="postGlow" cx="55%" cy="60%" r="60%">
          <stop offset="0" stop-color="#b5501c"/>
          <stop offset=".45" stop-color="#5a2410"/>
          <stop offset="1" stop-color="#1d0d09"/>
        </radialGradient>
        <linearGradient id="postTop" x1="0" y1="0" x2="1" y2="1">
          <stop offset="0" stop-color="#eccdbb"/>
          <stop offset="1" stop-color="#fbeee6"/>
        </linearGradient>
        <linearGradient id="strip" x1="0" y1="0" x2="1" y2="0">
          <stop offset="0" stop-color="#eccdbb"/>
          <stop offset=".5" stop-color="#fbeee6"/>
          <stop offset="1" stop-color="#eccdbb"/>
        </linearGradient>
      </defs>
      <rect width="700" height="500" fill="url(#postGlow)"/>
      <path d="M0 0H700V300C560 300 420 180 0 150Z" fill="url(#postTop)"/>
      <path d="M0 150C420 180 560 300 700 300V312C560 312 420 194 0 164Z" fill="#d9a79c"/>
      <path d="M0 164C420 194 560 312 700 312V318C560 318 420 202 0 172Z" fill="#ffffff" opacity=".6"/>
      <line x1="548" y1="330" x2="674" y2="330" stroke="#b39a90" stroke-width="2" stroke-dasharray="2 4"/>
      <rect y="450" width="700" height="50" fill="url(#strip)"/>
    </svg>
    <p class="headline-lead">I AM HERE TO HANDLE ALL YOUR...</p>
    <h2 class="headline">AUCTION NEEDS!</h2>
    <div class="photo-slot cars-photo" role="img" aria-label="Photo of a row of cars lined up at an auto auction, blue, silver, yellow and red"></div>
    <div class="photo-slot gavel-photo" role="img" aria-label="Photo of an auction gavel on its block beside a small red model car"></div>
    <p class="call-script">Call me today &amp; let's get started!</p>
    <p class="experience">OVER 20 YEARS <strong>EXPERIENCE!</strong></p>
    <p class="body-copy">I have over 20 years of auction experience buying and selling for dealerships in North Carolina and Tennessee. Send me to the sale to either rep your vehicles or let me know what you need and I can be another set of eyes to help you buy what is hot and bad credit cars are my specialty. You know a car always sells better with a familiar face rather than auction personnel and with my great reputation I will be able to help find the buyers for your aged inventory.</p>
    <p class="contact-strip">CALL ME TODAY &amp; LET'S GET STARTED | ROB KELLNER | 555.287.6390</p>
  </section>

</body>
</html>
```